stickers for outdoor industry (brands like Veltrana, Kelso, Marlin) retail consultant

The main need that I need to solve: I am hosting a series of educational workshops at a trade show and I need a 2.5" diameter round sticker designed with my visual branding. In some additional designs, I'd like to see other shapes/sizes that occupy 4-8 sq inches of space.I am a specialty/independent retail consultant and I help small/local retailers run a more profitable business. My industry focus is on outdoor retailers (like small versions DTU) and the sticker is to be passed out at the main tradeshow that our industry has (think brands like Veltrana, Bivo, Kelso, Marlin, etc) I plan to put the stickers on the seats in the workshop and hope the attendees attach them to their water bottles, coolers, beer fridges, etc.I have the fonts and the background image--I just need some help with design, content, and the file to submit to the sticker printer. The name of my company is Hollow Pines (hollowpines.com to learn more). I need to use fonts Lulo Clean One Bold and Avenir Next LT Pro Light, which I have the permissions for.
I attached a mock up that is my vibe...but I'm open to other designs as well.
Updates
I'm also launching an industry networking group called THE GATHERING and would like a 2.5" round sticker design with the words "the gathering by hollow pines" "a community for specialty retailers" and/or other language from https://www.hollowpines.com/thegathering
Target Market(s)
retail buyers and owners of specialty outdoor retail shops; sales representatives of merchandise/brands that these retailers buy from. we buy/sell merchandise to aid our adventures in camping, hiking, trail running, global/adventure/urban travel, mountaineering, fishing, kayaking, SUP, etc
Industry/Entity Type
Retail
Font styles to use
Other font styles liked:
- lulo clean one bold, avenir next LTF light
Requirements
Must have
- -file that looks nice on 2.5" round sticker
- -other various designs that fit my target market
- -inspriational feel
- -a mix of my visual branding + your visual branding ideas if you're inspired
- -"HOLLOW PINES"
- -"hollowpines.com"
Nice to have
- Design 1) "resources for specialty retailers"
- Design 2) "support small business" or "support your local shop"
- Design 3) "THE GATHERING by HOLLOW PINES" "a community for specialty retailers"
- I like images that have sun rays or a wash of light in them
- maybe a few designs that have outdoorsy images or recreational activities in them
Should not have
- the words: consultant, consulting, agency, firm

```html
<!DOCTYPE html>
<html lang="en">
<head>
<meta charset="utf-8">
<title>Hollow Pines — Round Sticker Set</title>
<link href="https://fonts.googleapis.com/css2?family=Montserrat:wght@800&family=Nunito+Sans:wght@300;800&display=swap" rel="stylesheet">
<style>
  :root {
    --paper: #ffffff;
    --slate: #3a3638;
    --ink: #2f2a1c;
    --ring: #ffffff;
    --lilac-top: #f6f1f7;
    --lilac-mid: #e4d0e6;
    --lilac-low: #dcc1df;
    --teal-top: #eef7f6;
    --teal-mid: #a9d3cc;
    --teal-low: #72c8cb;
    --sun-top: #fcf8e4;
    --sun-mid: #ece0a0;
    --sun-low: #e1d07f;
  }
  * { box-sizing: border-box; margin: 0; padding: 0; }
  html, body { width: 1200px; height: 1200px; overflow: hidden; }
  body { position: relative; background: var(--paper); font-family: "Nunito Sans", sans-serif; }

  .backdrop-dark {
    position: absolute; left: 580px; top: 0; width: 620px; height: 1200px;
    background: var(--slate);
  }

  .sticker {
    position: absolute; width: 356px; height: 356px; border-radius: 50%;
    overflow: hidden; color: var(--ink); text-align: center;
  }
  .sticker--shadowed { box-shadow: 0 6px 26px rgba(0,0,0,0.18); }

  .sticker__scene { position: absolute; inset: 0; }
  .sticker--lilac .sticker__scene {
    background: linear-gradient(180deg, var(--lilac-top) 0%, var(--lilac-top) 18%, var(--lilac-mid) 40%, var(--lilac-low) 100%);
  }
  .sticker--teal .sticker__scene {
    background:
      radial-gradient(circle at 68% 22%, rgba(255,255,240,0.95) 0%, rgba(255,255,240,0) 30%),
      linear-gradient(180deg, var(--teal-top) 0%, var(--teal-top) 20%, var(--teal-mid) 42%, var(--teal-low) 100%);
  }
  .sticker--sun .sticker__scene {
    background:
      radial-gradient(circle at 70% 22%, rgba(255,255,250,0.95) 0%, rgba(255,255,250,0) 32%),
      linear-gradient(180deg, var(--sun-top) 0%, var(--sun-top) 18%, var(--sun-mid) 40%, var(--sun-low) 100%);
  }

  .sticker__ring { position: absolute; inset: 0; }

  .sticker__title {
    position: absolute; left: 0; right: 0; top: 134px;
    font-family: "Montserrat", sans-serif; font-weight: 800;
    font-size: 44px; line-height: 52px; letter-spacing: 0.14em;
    padding-left: 0.14em;
  }
  .sticker__tagline {
    position: absolute; left: 0; right: 0; top: 244px;
    font-weight: 300; font-size: 14.5px; line-height: 17px; letter-spacing: 0.01em;
  }
  .sticker__url {
    position: absolute; left: 0; right: 0; top: 288px;
    font-weight: 800; font-size: 8.5px; letter-spacing: 0.16em;
  }
</style>
</head>
<body>
  <div class="backdrop-dark"></div>

  <!-- white column -->
  <div class="sticker sticker--lilac sticker--shadowed" style="left:98px; top:38px;">
    <div class="sticker__scene" role="img" aria-label="Misty lilac mountain ridges fading into a pale sky"></div>
    <svg class="sticker__ring" viewBox="-178 -178 356 356" aria-hidden="true">
      <path d="M -150.2 -55 A 160 160 0 0 1 150.2 -55 M -155.4 38 A 160 160 0 0 0 155.4 38" fill="none" stroke="var(--ring)" stroke-width="1.6"/>
    </svg>
    <div class="sticker__title">HOLLOW<br>PINES</div>
    <div class="sticker__tagline">THE GATHERING<br>BY HOLLOW PINES</div>
    <div class="sticker__url">HOLLOWPINES.COM</div>
  </div>

  <div class="sticker sticker--teal sticker--shadowed" style="left:98px; top:428px;">
    <div class="sticker__scene" role="img" aria-label="Teal mountain ridges under a wash of morning sunlight"></div>
    <svg class="sticker__ring" viewBox="-178 -178 356 356" aria-hidden="true">
      <path d="M -150.2 -55 A 160 160 0 0 1 150.2 -55 M -155.4 38 A 160 160 0 0 0 155.4 38" fill="none" stroke="var(--ring)" stroke-width="1.6"/>
    </svg>
    <div class="sticker__title">HOLLOW<br>PINES</div>
    <div class="sticker__tagline">RESOURCES FOR<br>SPECIALTY RETAILERS</div>
    <div class="sticker__url">HOLLOWPINES.COM</div>
  </div>

  <div class="sticker sticker--sun sticker--shadowed" style="left:98px; top:812px;">
    <div class="sticker__scene" role="img" aria-label="Golden hazy mountain ridges with sun rays breaking through"></div>
    <svg class="sticker__ring" viewBox="-178 -178 356 356" aria-hidden="true">
      <path d="M -150.2 -55 A 160 160 0 0 1 150.2 -55 M -155.4 38 A 160 160 0 0 0 155.4 38" fill="none" stroke="var(--ring)" stroke-width="1.6"/>
    </svg>
    <div class="sticker__title">HOLLOW<br>PINES</div>
    <div class="sticker__tagline">SUPPORT YOUR<br>LOCAL SHOP</div>
    <div class="sticker__url">HOLLOWPINES.COM</div>
  </div>

  <!-- dark column -->
  <div class="sticker sticker--lilac" style="left:700px; top:36px;">
    <div class="sticker__scene" role="img" aria-label="Misty lilac mountain ridges fading into a pale sky"></div>
    <svg class="sticker__ring" viewBox="-178 -178 356 356" aria-hidden="true">
      <path d="M -150.2 -55 A 160 160 0 0 1 150.2 -55 M -155.4 38 A 160 160 0 0 0 155.4 38" fill="none" stroke="var(--ring)" stroke-width="1.6"/>
    </svg>
    <div class="sticker__title">HOLLOW<br>PINES</div>
    <div class="sticker__tagline">THE GATHERING<br>BY HOLLOW PINES</div>
    <div class="sticker__url">HOLLOWPINES.COM</div>
  </div>

  <div class="sticker sticker--teal" style="left:700px; top:428px;">
    <div class="sticker__scene" role="img" aria-label="Teal mountain ridges under a wash of morning sunlight"></div>
    <svg class="sticker__ring" viewBox="-178 -178 356 356" aria-hidden="true">
      <path d="M -150.2 -55 A 160 160 0 0 1 150.2 -55 M -155.4 38 A 160 160 0 0 0 155.4 38" fill="none" stroke="var(--ring)" stroke-width="1.6"/>
    </svg>
    <div class="sticker__title">HOLLOW<br>PINES</div>
    <div class="sticker__tagline">RESOURCES FOR<br>SPECIALTY RETAILERS</div>
    <div class="sticker__url">HOLLOWPINES.COM</div>
  </div>

  <div class="sticker sticker--sun" style="left:700px; top:820px;">
    <div class="sticker__scene" role="img" aria-label="Golden hazy mountain ridges with sun rays breaking through"></div>
    <svg class="sticker__ring" viewBox="-178 -178 356 356" aria-hidden="true">
      <path d="M -150.2 -55 A 160 160 0 0 1 150.2 -55 M -155.4 38 A 160 160 0 0 0 155.4 38" fill="none" stroke="var(--ring)" stroke-width="1.6"/>
    </svg>
    <div class="sticker__title">HOLLOW<br>PINES</div>
    <div class="sticker__tagline">SUPPORT YOUR<br>LOCAL SHOP</div>
    <div class="sticker__url">HOLLOWPINES.COM</div>
  </div>
</body>
</html>
```